Celestine Varga Gymnastics Center Business Card

Develop a business card with my CV logo provided. A classy and unique design using the colors black, white, purple and maybe a splash of gold. Add Address (918 S. Harlan Lane Medina, Ohio 44871), email (CelestineVargaGymnasticsCtr@mailbrook.com, website (www.CelestineVargaGymnasticsCenter.com), phone number (330-555-0192) on the card. Social media if there's room also. t: @VargaGym, i: @VargaGym, f: @CelestineVargaGymnasticsCenter

Target Market(s)

Families, children, gymnastics community and beyond

Industry/Entity Type

Business

Contact Information for Business Card

Add name (Celestine Varga) who is the owner. Add logo, add address details, classy font, uniqueness important, rounded edges on business card. Horizontal business card needed.

Font styles to use
Serif
Sans Serif

Colors
6b449b
ffffff

Requirements
Must have
• Must have logo, owner name and owner on card, must have colors purple, white, black where needed in print, and a splash of gold if appropriate. Keep card classy and clean. Must have address of location, phone number, website of business, email and social media.
Nice to have
• I am open here, but I'd appreciate uniqueness. Must be a lasting image for branding...
Should not have
• No kid-like looks...

```html
<!DOCTYPE html>
<html lang="en">
<head>
<meta charset="utf-8">
<title>Celestine Varga Gymnastics Center — Business Card</title>
<link rel="stylesheet" href="https://fonts.googleapis.com/css2?family=Noto+Serif:wght@400;600&display=swap">
<style>
  :root {
    --page: #eeecea;
    --card: #141414;
    --ink: #ffffff;
    --purple: #6b449b;
    --purple-light: #8a5cc4;
    --gold: #d9b43f;
  }
  * { box-sizing: border-box; margin: 0; padding: 0; }
  html, body { width: 1200px; height: 1200px; overflow: hidden; }
  body {
    background: var(--page);
    font-family: "Noto Serif", Georgia, serif;
    display: flex;
    flex-direction: column;
    align-items: center;
    justify-content: center;
    gap: 56px;
  }
  .card {
    position: relative;
    width: 900px;
    height: 514px;
    background: var(--card);
    border-radius: 40px;
    color: var(--ink);
    overflow: hidden;
  }

  /* Back of card */
  .card-back {
    display: flex;
    align-items: center;
    justify-content: center;
    gap: 28px;
  }
  .back-mark {
    width: 70px; height: 70px;
    border-radius: 50%;
    background: var(--gold);
    flex: none;
  }
  .back-name {
    color: var(--gold);
    font-weight: 600;
    font-size: 46px;
    line-height: 1.15;
    text-transform: uppercase;
    letter-spacing: 1px;
  }

  /* Front of card */
  .owner {
    position: absolute;
    right: 62px;
    top: 62px;
    text-align: right;
  }
  .owner-name {
    font-size: 50px;
    font-weight: 400;
    letter-spacing: 1px;
    text-transform: uppercase;
    line-height: 1;
  }
  .owner-title {
    font-size: 19px;
    text-transform: uppercase;
    letter-spacing: 1px;
    margin-top: 6px;
  }
  .divider {
    position: absolute;
    left: 336px;
    top: 190px;
    width: 3px;
    height: 276px;
    background: var(--ink);
  }
  .contact-list {
    position: absolute;
    left: 360px;
    top: 196px;
    list-style: none;
  }
  .contact-item {
    display: flex;
    align-items: center;
    gap: 16px;
    height: 38px;
    font-size: 18.5px;
  }
  .contact-icon {
    width: 24px; height: 24px;
    flex: none;
    fill: none;
    stroke: var(--ink);
    stroke-width: 2;
    stroke-linecap: round;
    stroke-linejoin: round;
  }
  .social-dot {
    width: 16px; height: 16px;
    margin: 0 4px;
    border-radius: 50%;
    background: var(--ink);
    flex: none;
  }
  .brand {
    position: absolute;
    left: 46px;
    bottom: 62px;
    width: 270px;
  }
  .brand-row {
    display: flex;
    align-items: center;
    gap: 14px;
  }
  .brand-mark {
    width: 40px; height: 40px;
    border-radius: 50%;
    background: var(--purple);
    flex: none;
  }
  .brand-name {
    font-size: 19px;
    font-weight: 600;
    line-height: 1.15;
    text-transform: uppercase;
    color: var(--ink);
  }
  .brand-tagline {
    margin-top: 8px;
    font-size: 15px;
    color: var(--purple-light);
  }
</style>
</head>
<body>

  <section class="card card-back" aria-label="Business card back">
    <span class="back-mark"></span>
    <div class="back-name">Celestine Varga<br>Gymnastics Center</div>
  </section>

  <section class="card card-front" aria-label="Business card front">
    <header class="owner">
      <h1 class="owner-name">Celestine Varga</h1>
      <p class="owner-title">Personal Coach</p>
    </header>

    <div class="brand">
      <div class="brand-row">
        <span class="brand-mark"></span>
        <div class="brand-name">Celestine Varga<br>Gymnastics Center</div>
      </div>
      <p class="brand-tagline">Gymnastics, Camps, Yoga &amp; More</p>
    </div>

    <div class="divider"></div>

    <ul class="contact-list">
      <li class="contact-item">
        <svg class="contact-icon" viewBox="0 0 24 24"><path d="M5 3h4l2 5-2.5 1.5a11 11 0 0 0 6 6L16 13l5 2v4a2 2 0 0 1-2 2A17 17 0 0 1 3 5a2 2 0 0 1 2-2z"/></svg>
        <span>330-555-0192</span>
      </li>
      <li class="contact-item">
        <svg class="contact-icon" viewBox="0 0 24 24"><path d="M12 22s7-7 7-12a7 7 0 0 0-14 0c0 5 7 12 7 12z"/><circle cx="12" cy="10" r="2.5"/></svg>
        <span>918 S. Harlan Lane Medina, Ohio 44871</span>
      </li>
      <li class="contact-item">
        <svg class="contact-icon" viewBox="0 0 24 24"><rect x="3" y="5" width="18" height="14" rx="1"/><path d="M3 6l9 7 9-7"/></svg>
        <span>CelestineVargaGymnasticsCtr@mailbrook.com</span>
      </li>
      <li class="contact-item">
        <span class="social-dot"></span>
        <span>@CelestineVargaGymnasticsCenter</span>
      </li>
      <li class="contact-item">
        <span class="social-dot"></span>
        <span>@VargaGym</span>
      </li>
      <li class="contact-item">
        <span class="social-dot"></span>
        <span>@VargaGym</span>
      </li>
      <li class="contact-item">
        <svg class="contact-icon" viewBox="0 0 24 24"><circle cx="12" cy="12" r="9"/><path d="M3 12h18M12 3c3 3 3 15 0 18M12 3c-3 3-3 15 0 18"/></svg>
        <span>www.CelestineVargaGymnasticsCenter.com</span>
      </li>
    </ul>
  </section>

</body>
</html>
```